Local Motorsports Photography Business Card Design

Looking for a Logo and Business Card design for my father who is a local photographer based in Perth operating under the business name "KLR Photography". Specializing in Motorsports (Torque Racers/Hyperwheels/Corvan Trial) and events photography.
Would like it to look professional, while still maintaining a local/personal feel. Color\Design of the Logo and Card are open to your own interpretation, but should limit the color scheme to around 2-3 colors.
Design should be a logo one side and contact details on the rear. The website currently is very simple and a generic template and should not be used as a basis for design.
Industry/Entity Type
Business
Contact Information for Business Card
Name: Malcolm Purdie
Website: www.klrphotography-example.com.au
Email: malcolm@klrphotography-example.com.au
Phone: 0471 629 385
Look and feel
Each slider illustrates characteristics of the customer's brand and the style your logo design should communicate.

```html
<!DOCTYPE html>
<html lang="en">
<head>
<meta charset="utf-8">
<title>KLR Photography – Business Card</title>
<link href="https://fonts.googleapis.com/css2?family=Signika:wght@600;700&family=Quicksand:wght@500&display=swap" rel="stylesheet">
<style>
  :root {
    --page-bg: #ecebe8;
    --navy-deep: #0c0f24;
    --navy: #1b2143;
    --copper: #b7773a;
    --name-yellow: #f3e321;
    --white: #ffffff;
    --ink: #111111;
    --track-grey: #8a9099;
    --grass: #9fb06b;
    --blur-red: #c4332c;
    --blur-sky: #d9e3ea;
  }
  * { box-sizing: border-box; margin: 0; padding: 0; }
  html, body {
    width: 1200px; height: 1200px; overflow: hidden;
    background: var(--page-bg);
  }
  .sheet {
    width: 1200px; height: 1200px;
    display: flex; flex-direction: column; align-items: center; justify-content: center;
    gap: 40px;
  }
  .card {
    position: relative;
    width: 960px; height: 548px;
    overflow: hidden;
    box-shadow: 0 6px 18px rgba(0,0,0,0.18);
  }

  /* Front side */
  .card-front .front-photo {
    position: absolute; inset: 0;
    background:
      radial-gradient(ellipse 45% 30% at 55% 62%, var(--blur-red), transparent 70%),
      linear-gradient(170deg, var(--blur-sky) 0%, #c9c3b4 40%, #8b7d67 70%, #5f5a4c 100%);
  }
  .front-logo {
    position: absolute; left: 50%; top: 42%;
    transform: translate(-50%, -50%);
    display: flex; align-items: center; gap: 26px;
  }
  .logo-dot {
    flex: none;
    width: 96px; height: 96px; border-radius: 50%;
    background: var(--ink);
  }
  .logo-name {
    font-family: "Signika", sans-serif; font-weight: 700;
    font-size: 72px; line-height: 1; color: var(--ink);
    white-space: nowrap;
  }

  /* Back side */
  .card-back {
    background: linear-gradient(135deg, var(--navy) 0%, var(--navy-deep) 100%);
  }
  .back-logo {
    position: absolute; left: 56px; top: 52px;
    display: flex; align-items: center; gap: 20px;
  }
  .back-logo .logo-dot { width: 74px; height: 74px; background: var(--white); }
  .back-logo .logo-name { font-size: 50px; color: var(--white); }

  .race-photo {
    position: absolute;
    left: 570px; top: 20px;
    width: 460px; height: 460px; border-radius: 50%;
    border: 12px solid var(--copper);
    background: linear-gradient(180deg, var(--grass) 0%, var(--grass) 38%, var(--track-grey) 55%, #6f747c 100%);
  }

  .contact {
    position: absolute; left: 62px; top: 292px;
    font-family: "Signika", sans-serif; font-weight: 700;
    color: var(--white);
  }
  .contact-name {
    font-size: 32px; color: var(--name-yellow); margin-bottom: 12px;
  }
  .contact-line { font-size: 21px; line-height: 1.75; white-space: nowrap; }

  .website {
    position: absolute; right: 34px; bottom: 18px;
    font-family: "Quicksand", sans-serif; font-weight: 500;
    font-size: 22px; color: var(--white);
  }
</style>
</head>
<body>
<main class="sheet">
  <section class="card card-front" aria-label="Business card front">
    <div class="front-photo" role="img" aria-label="Motion-blurred photograph of a red race car on track"></div>
    <div class="front-logo">
      <span class="logo-dot"></span>
      <span class="logo-name">KLR Photography</span>
    </div>
  </section>

  <section class="card card-back" aria-label="Business card back">
    <div class="back-logo">
      <span class="logo-dot"></span>
      <span class="logo-name">KLR Photography</span>
    </div>
    <div class="race-photo" role="img" aria-label="Photograph of two superbikes leaning into a corner on a race track"></div>
    <div class="contact">
      <p class="contact-name">Malcolm Purdie</p>
      <p class="contact-line">Email: malcolm@klrphotography-example.com.au</p>
      <p class="contact-line">Phone: 0471 629 385</p>
    </div>
    <p class="website">www.klrphotography-example.com.au</p>
  </section>
</main>
</body>
</html>
```